furniture and home contents restoration

I need to list the services that we perform in our studio.
we serve the general public as well as the insurance/ remediation industry

```html
<!DOCTYPE html>
<html lang="en">
<head>
<meta charset="utf-8">
<title>Paramount Restorers – Business Card</title>
<link href="https://fonts.googleapis.com/css2?family=Cinzel:wght@400;600&family=Roboto:wght@400;500;700&display=swap" rel="stylesheet">
<style>
  :root {
    --slate: #1f2d33;
    --plum: #8e4f80;
    --white: #ffffff;
    --ink: #1f2d33;
    --muted: #5a6469;
    --backdrop: #3b3d3f;
  }
  * { box-sizing: border-box; margin: 0; padding: 0; }
  html, body {
    width: 1200px; height: 900px; overflow: hidden;
    background: var(--backdrop);
  }
  body { position: relative; font-family: "Roboto", Arial, sans-serif; }

  .card {
    position: absolute; left: 270px;
    width: 660px; height: 377px;
    border-radius: 20px; overflow: hidden;
    box-shadow: 0 10px 30px rgba(0,0,0,.35);
  }

  /* ---------- Back: services ---------- */
  .card-back { top: 50px; background: var(--slate); color: var(--white); }
  .card-back .brand {
    position: absolute; top: 26px; left: 250px;
    display: flex; align-items: center; gap: 12px;
  }
  .brand-square { width: 40px; height: 40px; background: var(--plum); }
  .brand-divider { width: 1px; height: 44px; background: rgba(255,255,255,.5); }
  .brand-name {
    font-family: "Cinzel", Georgia, serif; font-weight: 600;
    font-size: 21px; line-height: 1; letter-spacing: 1px; text-transform: uppercase;
  }
  .brand-tag {
    font-family: "Cinzel", Georgia, serif; font-size: 9px;
    letter-spacing: 1.5px; text-transform: uppercase; margin-top: 5px; opacity: .8;
  }
  .services-heading {
    position: absolute; top: 96px; left: 36px;
    font-family: "Cinzel", Georgia, serif; font-size: 17px; letter-spacing: 1.5px;
  }
  .services-rule {
    position: absolute; top: 124px; left: 36px; width: 590px; height: 1px;
    background: var(--plum);
  }
  .services-list {
    position: absolute; list-style: none;
    font-size: 10.5px; line-height: 16px; letter-spacing: .4px; text-transform: uppercase;
  }
  .services-list.col-left { top: 132px; left: 36px; }
  .services-list.col-right { top: 132px; left: 330px; }
  .services-band {
    position: absolute; left: 0; bottom: 0; width: 100%; height: 72px;
    background: var(--plum);
    display: flex; flex-direction: column; justify-content: center; align-items: center;
    font-size: 11.5px; line-height: 18px; letter-spacing: .6px; text-transform: uppercase;
  }

  /* ---------- Front: contact ---------- */
  .card-front { top: 473px; background: var(--white); color: var(--ink); }
  .card-front .brand {
    position: absolute; top: 34px; left: 40px;
    display: flex; align-items: center; gap: 18px;
  }
  .card-front .brand-square { width: 64px; height: 64px; }
  .card-front .brand-divider { height: 70px; background: var(--ink); }
  .card-front .brand-name { font-size: 34px; color: var(--ink); }
  .card-front .brand-tag { font-size: 12px; color: var(--muted); opacity: 1; margin-top: 8px; }
  .address {
    position: absolute; top: 132px; right: 40px; text-align: right;
    font-size: 15px; line-height: 21px; color: var(--ink);
  }
  .person-name {
    position: absolute; top: 190px; left: 40px;
    font-family: "Cinzel", Georgia, serif; font-weight: 600; font-size: 20px; letter-spacing: 1.5px;
  }
  .person-rule {
    position: absolute; top: 222px; left: 40px; width: 580px; height: 1px; background: var(--ink);
  }
  .contacts { position: absolute; top: 230px; left: 40px; list-style: none; }
  .contacts li {
    display: flex; align-items: center; gap: 10px;
    font-size: 15px; line-height: 22px; letter-spacing: .8px;
  }
  .contacts svg { width: 14px; height: 14px; fill: var(--plum); flex: none; }
  .front-band {
    position: absolute; left: 0; bottom: 0; width: 100%; height: 52px;
    background: var(--slate); color: var(--white); text-align: center;
    display: flex; flex-direction: column; justify-content: center;
    text-transform: uppercase; letter-spacing: .8px;
  }
  .front-band .mission { font-size: 13px; line-height: 17px; }
  .front-band .tenure { font-size: 13px; line-height: 17px; font-weight: 700; }
</style>
</head>
<body>

<section class="card card-back" aria-label="Card back – services">
  <div class="brand">
    <div class="brand-square"></div>
    <div class="brand-divider"></div>
    <div>
      <div class="brand-name">Paramount Restorers</div>
      <div class="brand-tag">Home Contents Restoration</div>
    </div>
  </div>

  <h2 class="services-heading">OUR SERVICES</h2>
  <div class="services-rule"></div>

  <ul class="services-list col-left">
    <li>Antique repair and restoration</li>
    <li>Art cleaning and remounting</li>
    <li>Art and mirror frame repair</li>
    <li>Chandelier cleaning and restoration</li>
    <li>Document restoration</li>
    <li>Glass, ceramic, and mirror repair</li>
    <li>Hardware repair and restoration</li>
    <li>Kitchen removal and reinstallation</li>
    <li>Lamp cleaning and restoration</li>
    <li>Lamp shade replacement</li>
  </ul>
  <ul class="services-list col-right">
    <li>Metal polishing and restoration</li>
    <li>Odor removal and ozone services</li>
    <li>Photo restoration</li>
    <li>Upholstery cleaning and deodorizing</li>
    <li>In-house upholstery and reupholstery</li>
    <li>Rug cleaning and restoration</li>
    <li>Musical instrument restoration</li>
    <li>Window treatment repair/ restoration</li>
    <li>Leather restoration and replacement</li>
    <li>Piano restoration and repair</li>
  </ul>

  <div class="services-band">
    <span>On-site inspections and desk review services</span>
    <span>Assessment reports and estimates for repair and restoration</span>
  </div>
</section>

<section class="card card-front" aria-label="Card front – contact">
  <div class="brand">
    <div class="brand-square"></div>
    <div class="brand-divider"></div>
    <div>
      <div class="brand-name">Paramount Restorers</div>
      <div class="brand-tag">Home Contents Restoration</div>
    </div>
  </div>

  <address class="address" style="font-style:normal">
    128 Brookline Mill Rd<br>Ashford, NY 10590
  </address>

  <h1 class="person-name">DANIEL MORETTI</h1>
  <div class="person-rule"></div>

  <ul class="contacts">
    <li>
      <svg viewBox="0 0 24 24" aria-label="Office phone"><path d="M6.6 10.8a15.1 15.1 0 0 0 6.6 6.6l2.2-2.2c.3-.3.7-.4 1-.2 1.1.4 2.3.6 3.6.6.6 0 1 .4 1 1V20c0 .6-.4 1-1 1A17 17 0 0 1 3 4c0-.6.4-1 1-1h3.5c.6 0 1 .4 1 1 0 1.3.2 2.5.6 3.6.1.3 0 .7-.2 1z"/></svg>
      555.210.4400
    </li>
    <li>
      <svg viewBox="0 0 24 24" aria-label="Mobile"><path d="M7 1h10a2 2 0 0 1 2 2v18a2 2 0 0 1-2 2H7a2 2 0 0 1-2-2V3a2 2 0 0 1 2-2zm0 3v15h10V4zm5 16.2a1 1 0 1 0 0 .01z"/></svg>
      555.318.7720
    </li>
    <li>
      <svg viewBox="0 0 24 24" aria-label="Fax"><path d="M7 2h10v5H7zM4 8h16a2 2 0 0 1 2 2v7h-4v5H6v-5H2v-7a2 2 0 0 1 2-2zm4 8v4h8v-4z"/></svg>
      555.210.4460
    </li>
    <li>
      <svg viewBox="0 0 24 24" aria-label="Email"><path d="M2 5h20v14H2zm2 2v.5l8 5 8-5V7zm0 2.8V17h16V9.8l-8 5z"/></svg>
      studio@paramountrestorers.com
    </li>
  </ul>

  <div class="front-band">
    <span class="mission">Serving the general public and the insurance industry</span>
    <span class="tenure">For over 40 years</span>
  </div>
</section>

</body>
</html>
```